Law Firm Website

I currently have a temporary site that I created myself at www.mcorveyfirm.net (hosted by 9tree). I am generally happy with the content.

My permanent website just has basic information right now: www.mcorveyfirm.com (hosted by lumenrack). I want to take the general content from the temporary website and have a more professional looking website on the permanent website. I want it in Wordpress format. I want a link to my blog: www.crookedpath.com. I want it to work on pads and smart phones. My number and e-mail address should be available on every page. The idea is to feature the potential client more than the lawyer.
Updates

Several of the designs are good. I would like the front page to have my number and address at the top (and at the top of every page) and to identify my law firm as "Law Office of Gerald T. Corvey". No need to include "mcorveyfirm" as that is just the web address. I like showing the most recent blog posts on the front page. I don't need video. No need to emphasize office hours or map location on the front page (that could be under a contact button). My picture should be somewhere. I would like an image from Boston on the front page if we can find one that is not copyright protected. No images of gavels or scales of justice. See some of the sample websites I listed in previous messages. Thanks!

Industry/Entity Type

Law Firm

```html
<!DOCTYPE html>
<html lang="en">
<head>
<meta charset="utf-8">
<title>Law Office of Gerald T. Corvey</title>
<link href="https://fonts.googleapis.com/css2?family=Bebas+Neue&family=Josefin+Sans:wght@400;600&family=Arimo:wght@400;700&display=swap" rel="stylesheet">
<style>
:root{
  --orange:#f07a0c;
  --black:#0c0c0c;
  --dark:#1a1a1a;
  --page:#f6f6f6;
  --line:#dedede;
  --text:#555;
  --muted:#9a9a9a;
  --white:#fff;
}
*{margin:0;padding:0;box-sizing:border-box}
html,body{width:877px;height:1200px;overflow:hidden}
body{position:relative;background:var(--page);font-family:"Arimo",Arial,sans-serif;color:var(--text)}
.abs{position:absolute}

/* navigation */
.topnav{left:0;top:0;width:877px;height:36px;background:rgba(20,14,12,.92);border-top:2px solid var(--orange);z-index:2}
.topnav ul{list-style:none;display:flex;justify-content:space-between;position:absolute;left:62px;top:0;width:740px;height:34px}
.topnav li{font-size:9.5px;color:var(--white);line-height:34px;white-space:nowrap}
.topnav li.active{background:var(--orange);padding:0 10px}

/* hero */
.hero-photo{left:0;top:0;width:877px;height:355px;background:linear-gradient(120deg,#2a1a14 0%,#5c3324 35%,#8a5438 60%,#3a2218 100%)}
.site-title{left:0;top:88px;width:877px;text-align:center;font-family:"Josefin Sans",sans-serif;font-weight:400;font-size:58px;color:var(--white)}
.title-rule{left:161px;top:156px}
.office-name{left:0;top:224px;width:877px;text-align:center;font-family:"Bebas Neue",sans-serif;font-weight:400;font-size:36px;color:var(--white);letter-spacing:.5px}

/* consultation band */
.consult-band{left:0;top:355px;width:877px;height:110px;background:rgba(15,12,10,.85)}
.consult-title{left:62px;top:376px;font-family:"Bebas Neue",sans-serif;font-size:34px;line-height:32px;color:var(--white)}
.toll-label{left:262px;top:381px;font-family:"Bebas Neue",sans-serif;font-size:19px;color:var(--orange)}
.toll-number{left:262px;top:404px;font-family:"Bebas Neue",sans-serif;font-size:40px;color:var(--white);letter-spacing:.5px}
.hours-note{left:464px;top:392px;font-size:12px;line-height:18px;color:var(--white)}
.chat-box{left:573px;top:355px;width:240px;height:110px;background:var(--black)}
.chat-title{left:593px;top:372px;font-family:"Bebas Neue",sans-serif;font-size:36px;line-height:38px;color:var(--white)}
.chat-go{left:671px;top:377px;width:33px;height:26px;background:var(--orange)}

/* practice boxes */
.practice{top:507px;width:176px;height:170px;border:1px solid var(--line);background:var(--page);text-align:center}
.practice h3{margin-top:22px;font-family:"Josefin Sans",sans-serif;font-weight:400;font-size:16px;line-height:20px;color:#333}
.practice p{margin:8px 14px 0;font-size:11px;line-height:15px;color:var(--text)}
.practice .more{display:block;margin-top:14px;font-size:9px;color:#555}
.practice-icon{top:490px;width:22px;height:22px;background:var(--page)}

.headline{left:0;top:696px;width:877px;text-align:center;font-family:"Josefin Sans",sans-serif;font-weight:400;font-size:27px;line-height:30px;color:var(--orange)}

/* team band */
.team-band{left:0;top:768px;width:877px;height:201px;background:var(--black)}
.team-arrow{top:793px;width:25px;height:25px;background:var(--orange)}
.team-photo{top:837px;width:107px;height:107px;background:linear-gradient(160deg,#e4e4e4,#9a9a9a 70%,#5e5e5e)}

/* footer */
.footer-col{top:990px}
.footer-col h4{font-family:"Josefin Sans",sans-serif;font-weight:400;font-size:16px;color:var(--orange);margin-bottom:10px}
.footer-col p{font-size:10px;line-height:19px;color:var(--muted)}
.footer-col p.email{color:var(--orange)}
.social{display:flex;gap:6px;margin-top:6px}
.social span{width:22px;height:22px;border-radius:50%;background:#d4d4d4}
.bottom-bar{left:0;top:1161px;width:877px;height:39px;background:var(--orange);color:var(--white);font-size:10px}
.bottom-bar .copy{position:absolute;left:62px;top:14px}
.bottom-bar .credit{position:absolute;right:62px;top:14px}
</style>
</head>
<body>

<div class="abs hero-photo" role="img" aria-label="Warm-toned photograph of law books on a desk"></div>

<nav class="abs topnav">
  <ul>
    <li class="active">HOME</li><li>WHY HIRE ME?</li><li>SUCCESS STORIES</li><li>PRACTICE AREAS</li><li>REPRESENTATIVE CLIENTS</li><li>SERVICES PROVIDED</li><li>CONTACT US</li><li>HOW TO FIND US</li>
  </ul>
</nav>

<h1 class="abs site-title">Gerald T. Corvey</h1>
<svg class="abs title-rule" width="555" height="14" viewBox="0 0 555 14">
  <line x1="0" y1="7" x2="555" y2="7" stroke="#fff" stroke-width="1"/>
  <line x1="0" y1="7" x2="60" y2="7" stroke="#fff" stroke-width="3"/>
  <line x1="495" y1="7" x2="555" y2="7" stroke="#fff" stroke-width="3"/>
  <circle cx="271" cy="7" r="3.5" fill="#fff"/><circle cx="284" cy="7" r="3.5" fill="#fff"/>
</svg>
<h2 class="abs office-name">LAW OFFICE OF GERALD T. CORVEY</h2>

<section class="abs consult-band"></section>
<div class="abs consult-title">GET FREE LEGAL<br>CONSULTATION:</div>
<div class="abs toll-label">CALL US TOLL FREE:</div>
<div class="abs toll-number">617 555-0142</div>
<div class="abs hours-note">7 days a week<br>from 8:00 am<br>to 2:00 am</div>
<div class="abs chat-box"></div>
<div class="abs chat-title">24/7<br>OUR SUPPORT CHAT</div>
<svg class="abs chat-go" viewBox="0 0 33 26"><path d="M14 9 L20 13 L14 17 Z" fill="#fff"/></svg>

<div class="abs practice" style="left:62px"><h3>PROTECTING AND<br>DEFENDING</h3><p>Lorem ipsum dolor sit amet, consectetuer adipiscing elit, sed diam nonummy nibh.</p><span class="more">READ MORE</span></div>
<div class="abs practice" style="left:255px"><h3>ROGUE<br>EMPLOYEES</h3><p>Lorem ipsum dolor sit amet, consectetuer adipiscing elit, sed diam nonummy nibh.</p><span class="more">READ MORE</span></div>
<div class="abs practice" style="left:447px"><h3>CHEATING<br>BUSINESS PARTNERS</h3><p>Lorem ipsum dolor sit amet, consectetuer adipiscing elit, sed diam nonummy nibh.</p><span class="more">READ MORE</span></div>
<div class="abs practice" style="left:639px"><h3>GOVERNMENT<br>AGENCIES</h3><p>Lorem ipsum dolor sit amet, consectetuer adipiscing elit, sed diam nonummy nibh.</p><span class="more">READ MORE</span></div>
<svg class="abs practice-icon" style="left:139px" viewBox="0 0 22 22"><circle cx="11" cy="7" r="4" fill="#444"/><path d="M4 19 Q11 9 18 19 Z" fill="#444"/></svg>
<svg class="abs practice-icon" style="left:332px" viewBox="0 0 22 22"><circle cx="11" cy="7" r="4" fill="#444"/><path d="M4 19 Q11 9 18 19 Z" fill="#444"/></svg>
<svg class="abs practice-icon" style="left:524px" viewBox="0 0 22 22"><circle cx="11" cy="7" r="4" fill="#444"/><path d="M4 19 Q11 9 18 19 Z" fill="#444"/></svg>
<svg class="abs practice-icon" style="left:716px" viewBox="0 0 22 22"><circle cx="11" cy="7" r="4" fill="#444"/><path d="M4 19 Q11 9 18 19 Z" fill="#444"/></svg>

<h2 class="abs headline">FOUNDED IN 1956, OUR AGENCY<br>HAS OVER 200 LAWYERS</h2>

<section class="abs team-band"></section>
<svg class="abs team-arrow" style="left:412px" viewBox="0 0 25 25"><path d="M15 8 L10 12.5 L15 17 Z" fill="#fff"/></svg>
<svg class="abs team-arrow" style="left:440px" viewBox="0 0 25 25"><path d="M10 8 L15 12.5 L10 17 Z" fill="#fff"/></svg>
<div class="abs team-photo" style="left:62px" role="img" aria-label="Black and white portrait of a team lawyer"></div>
<div class="abs team-photo" style="left:191px" role="img" aria-label="Black and white portrait of a team lawyer"></div>
<div class="abs team-photo" style="left:320px" role="img" aria-label="Black and white portrait of a team lawyer"></div>
<div class="abs team-photo" style="left:450px" role="img" aria-label="Black and white portrait of a team lawyer"></div>
<div class="abs team-photo" style="left:579px" role="img" aria-label="Black and white portrait of a team lawyer"></div>
<div class="abs team-photo" style="left:708px" role="img" aria-label="Black and white portrait of a team lawyer"></div>

<div class="abs footer-col" style="left:62px">
  <h4>Contact Us</h4>
  <p>Law Office of Gerald T. Corvey<br>48 Alder St.<br>4th Floor<br>Boston, MA 02109<br>Phone: 617 555-0142<br>Fax: 857 555-0199</p>
  <p class="email">Email: gcorvey@mcorveyfirm.com</p>
</div>
<div class="abs footer-col" style="left:352px">
  <h4>Office Hours</h4>
  <p>We can be reached during the<br>following hours:<br>Monday Thru Friday 10am-6pm</p>
</div>
<div class="abs footer-col" style="left:641px">
  <h4>New Online Presentation</h4>
  <p>Under Construction<br>More news</p>
  <h4 style="margin-top:14px;margin-bottom:4px">Follow Us</h4>
  <div class="social"><span></span><span></span><span></span><span></span></div>
</div>

<footer class="abs bottom-bar">
  <span class="copy">Copyright © 2014 Gerald T. Corvey / All Reserved</span>
  <span class="credit">Designed &amp; Developed By PixelFold</span>
</footer>

</body>
</html>
```